Web design for Velto Staffworks

We need to redesign and update the website for www.veltostaffworks.io, if you'll look, you can see it is very poorly done.

The content won't change much (the founders page will go away though). I've attached a logo and flyer we are using that may provide inspiration for the design, though you don't have to make it consistent with the flyer.

Industry/Entity Type

Hr technology

Coding

Coded - Design and coding required

Number of Pages Required

5+ page

Requirements
Must have
• To be hosted with NimbaHost

```html
<!DOCTYPE html>
<html lang="en">
<head>
<meta charset="utf-8">
<title>Velto Staffworks — HR Analytics Platform</title>
<link href="https://fonts.googleapis.com/css2?family=Jost:wght@400;500;600;700&family=Lato:wght@400;700&display=swap" rel="stylesheet">
<style>
:root{
  --blue:#12479c;
  --blue-deep:#0b3584;
  --navy:#1b3f7d;
  --footer:#133f83;
  --orange:#f5ab22;
  --orange-soft:#f3ac28;
  --ink:#1c2c4c;
  --muted:#4b5566;
  --page:#f5f5f5;
  --white:#ffffff;
}
*{margin:0;padding:0;box-sizing:border-box}
html,body{width:1200px;height:2854px;overflow:hidden}
body{position:relative;background:var(--page);font-family:"Lato",sans-serif;color:var(--ink)}
.abs{position:absolute}
.heading-font{font-family:"Jost",sans-serif}

/* hero */
.hero-bg{left:0;top:0;width:1200px;height:912px}
.hero-art{left:432px;top:150px;width:768px;height:510px;border-radius:50%;
  background:radial-gradient(ellipse at 55% 50%,#4fd0ff 0%,#1f7ee0 28%,#1557b8 55%,rgba(18,71,156,0) 75%)}
.brand-tab{left:73px;top:0;width:183px;height:181px}
.brand{display:flex;align-items:center;gap:8px;font-family:"Jost",sans-serif;font-weight:700;color:var(--blue)}
.brand-dot{width:26px;height:26px;border-radius:50%;background:var(--orange);flex:none}
.brand-head{left:88px;top:72px;font-size:19px}
.nav{left:0;top:52px;font-family:"Jost",sans-serif;font-size:14px;color:var(--white)}
.nav a{position:absolute;color:var(--white);text-decoration:none;white-space:nowrap}
.nav .active{font-weight:600}
.nav .active::after{content:"";position:absolute;left:0;right:0;bottom:-6px;height:2px;background:var(--white)}
.quote-btn{left:966px;top:42px;width:158px;height:40px;border-radius:20px;background:var(--orange);
  font-family:"Jost",sans-serif;font-weight:600;font-size:14px;color:var(--navy);display:flex;align-items:center;padding-left:22px;gap:10px}
.hero-kicker{left:78px;top:312px;font-family:"Jost",sans-serif;font-size:18px;color:var(--white)}
.hero-title{left:73px;top:338px;font-family:"Jost",sans-serif;font-size:39px;line-height:45px;color:var(--white);letter-spacing:.5px;font-weight:400}
.pill{border-radius:20px;display:flex;align-items:center;justify-content:center;font-family:"Jost",sans-serif;font-size:14px}
.hero-btn{left:74px;top:496px;width:155px;height:40px;background:var(--orange);color:var(--navy);font-weight:500}

/* about */
.about{left:114px;top:671px;width:975px;height:441px;background:var(--white);border:1px solid #e3e3e3}
.about-panel{left:600px;top:671px;width:489px;height:441px;background:var(--orange)}
.about-title{left:646px;top:724px;font-family:"Jost",sans-serif;font-weight:700;font-size:36px;color:var(--blue)}
.about-text{left:646px;top:799px;width:410px;font-size:14px;line-height:22px;color:#2b3550}
.read-btn{left:639px;top:1024px;width:154px;height:40px;background:var(--blue);color:var(--white)}
.diagram{left:114px;top:671px;width:486px;height:441px}
.diag-label{font-family:"Jost",sans-serif;font-weight:600;font-size:15px;fill:var(--navy)}

/* provide */
.provide-title{left:0;width:1200px;top:1208px;text-align:center;font-family:"Jost",sans-serif;font-weight:700;font-size:36px;color:var(--blue)}
.provide-sub{left:0;width:1175px;top:1255px;text-align:center;font-size:13.5px;line-height:16px;color:#333}
.card{width:308px}
.card svg.card-bg{position:absolute;left:0;top:0}
.card-icon{position:absolute;left:31px}
.card-title{position:absolute;left:33px;font-family:"Jost",sans-serif;font-weight:500;font-size:18px;line-height:21px;color:var(--navy)}
.card-text{position:absolute;left:33px;width:260px;font-size:13.5px;line-height:16px;color:#4a4f5a}
.card.is-featured .card-text{color:#5a3c06}
.go{position:absolute;left:29px;width:32px;height:32px;border-radius:50%;background:var(--navy);display:flex;align-items:center;justify-content:center}

/* cta band */
.cta{left:0;top:2240px;width:1200px;height:189px;background:linear-gradient(180deg,#f5ad25,#eea51f)}
.cta-line{left:0;width:1168px;text-align:center;font-family:"Jost",sans-serif;font-size:30px;line-height:28px;color:#fff6e3}
.cta-mail{left:426px;top:2360px;display:flex;align-items:center;gap:16px;font-family:"Jost",sans-serif;font-size:31px;color:var(--white)}

/* footer */
.footer{left:0;top:2429px;width:1200px;height:359px;background:var(--footer)}
.foot-tab{left:112px;top:2429px}
.foot-brand{left:136px;top:2590px;font-size:28px}
.foot-brand .brand-dot{width:36px;height:36px}
.foot-head{font-family:"Jost",sans-serif;font-weight:600;font-size:13px;color:var(--white);letter-spacing:.2px}
.foot-head::after{content:"";display:block;width:38px;height:2px;background:var(--orange);margin-top:8px}
.foot-links{left:434px;top:2566px;list-style:none;font-family:"Jost",sans-serif;font-size:14px;letter-spacing:1px;color:var(--white);line-height:22.5px}
.foot-links li::before{content:">";margin-right:10px}
.contact-row{left:618px;display:flex;align-items:center;gap:10px;font-size:13px;color:var(--white)}
.field{background:var(--white);border:1px solid #cfd6e4;font-family:"Jost",sans-serif;font-size:13px;color:#555;padding:8px 7px}
.send{left:813px;top:2669px;width:151px;height:32px;background:var(--orange);color:var(--blue);font-size:13px}

/* bottom bar */
.bottom{left:0;top:2788px;width:1200px;height:66px;background:#f3f3f3}
.copy{left:112px;top:2813px;font-family:"Jost",sans-serif;font-size:13px;color:#333}
.social{top:2803px;width:34px;height:34px;border-radius:50%;background:var(--navy)}
.social.first{background:var(--orange)}
</style>
</head>
<body>

<!-- hero -->
<svg class="abs hero-bg" viewBox="0 0 1200 912" aria-hidden="true">
  <defs>
    <linearGradient id="heroGrad" x1="0" y1="0" x2="1" y2="1">
      <stop offset="0" stop-color="#154d9f"/>
      <stop offset="1" stop-color="#0a2f78"/>
    </linearGradient>
  </defs>
  <polygon points="0,0 1200,0 1200,826 0,912" fill="url(#heroGrad)"/>
</svg>
<div class="abs hero-art" role="img" aria-label="Glowing cloud data platform illustration with circuit board, gears and security shield"></div>

<svg class="abs brand-tab" viewBox="0 0 183 181" aria-hidden="true"><polygon points="0,0 183,0 183,131 0,181" fill="#fff"/></svg>
<div class="abs brand brand-head" style="width:170px;flex-direction:column;gap:6px;left:80px;top:40px;text-align:center;font-size:18px">
  <span class="brand-dot" style="width:34px;height:34px"></span>
  <span>Velto Staffworks</span>
</div>

<nav class="abs nav">
  <a class="active" style="left:423px">Home</a>
  <a style="left:501px">Our Solutions</a>
  <a style="left:623px">Our Difference</a>
  <a style="left:758px">About Us</a>
  <a style="left:854px">Contact Us</a>
</nav>
<div class="abs quote-btn">Get A Quote
  <svg width="40" height="10" viewBox="0 0 40 10"><path d="M0 5H37M32 1L38 5L32 9" stroke="#1b3f7d" stroke-width="2" fill="none"/></svg>
</div>

<p class="abs hero-kicker">Stop Moving Data</p>
<h1 class="abs hero-title">Between System<br>Without Realizing<br>The Value of Insights.</h1>
<div class="abs pill hero-btn">Contact us</div>

<!-- about -->
<div class="abs about"></div>
<svg class="abs diagram" viewBox="0 0 486 441" aria-hidden="true">
  <g fill="none" stroke="#1b3f7d" stroke-width="1.6">
    <rect x="89" y="87" width="28" height="36" rx="2"/>
    <path d="M95 97H110M95 104H110M95 111H106"/>
    <circle cx="119" cy="113" r="6" stroke="#f5ab22"/>
    <rect x="352" y="84" width="44" height="30" rx="2"/>
    <circle cx="374" cy="80" r="5"/>
    <circle cx="363" cy="106" r="4" stroke="#f5ab22"/>
    <circle cx="374" cy="106" r="4" stroke="#f5ab22"/>
    <circle cx="385" cy="106" r="4" stroke="#f5ab22"/>
    <circle cx="186" cy="366" r="22"/>
    <path d="M186 366V344M186 366L203 379"/>
    <rect x="198" y="338" width="18" height="16" rx="2" stroke="#f5ab22"/>
  </g>
  <text x="108" y="152" class="diag-label" text-anchor="middle">ATS</text>
  <text x="378" y="143" class="diag-label" text-anchor="middle">HRIS/ Payroll</text>
  <text x="224" y="360" class="diag-label">KPIs/</text>
  <text x="224" y="378" class="diag-label">Data Vizulization</text>
  <g fill="none" stroke="#1b3f7d" stroke-width="1" stroke-dasharray="2 2">
    <path d="M112 166V197H152"/>
    <path d="M364 174V217H328"/>
    <path d="M243 295V325"/>
  </g>
  <g fill="#f5ab22">
    <path d="M112 160L109 166H115Z"/>
    <path d="M158 197L152 194V200Z"/>
    <path d="M364 168L361 174H367Z"/>
    <path d="M322 217L328 214V220Z"/>
    <path d="M243 331L240 325H246Z"/>
  </g>
  <circle cx="244" cy="215" r="22" fill="#f5ab22"/>
  <text x="244" y="256" text-anchor="middle" font-family="Jost, sans-serif" font-weight="700" font-size="20" fill="#12479c">Velto Staffworks</text>
  <text x="244" y="272" text-anchor="middle" font-family="Jost, sans-serif" font-size="7" fill="#1b3f7d" letter-spacing="1">HR ANALYTICS PLATFORM</text>
</svg>
<div class="abs about-panel"></div>
<h2 class="abs about-title">ABOUT US</h2>
<p class="abs about-text">Velto Staffworks gives you the ablity to make the most of your investment vin Payvista and Hirefield. By providing a seamless method of managing your master data between systems. clients get much than the simple movement of data from one system to another or keeping then is sync.information drives business decisions and by leveraging Velto Staffworks's suite of service, clients can quickly access real time information acress multiple systems. information that tradional data connection services move and lose. Every Transaction builds insight that drives value.</p>
<div class="abs pill read-btn">Read More</div>

<!-- provide -->
<h2 class="abs provide-title">WHAT WE PROVIDE</h2>
<p class="abs provide-sub">What we consider when<br>we create your repository of HR historical data</p>

<!-- row 1 -->
<div class="abs card" style="left:112px;top:1340px;height:373px">
  <svg class="card-bg" width="308" height="373"><polygon points="0,0 308,0 308,319 0,373" fill="#fff"/></svg>
  <svg class="card-icon" style="top:48px" width="90" height="90" viewBox="0 0 90 90" fill="none" stroke="#1b3f7d" stroke-width="2"><circle cx="45" cy="45" r="32"/><circle cx="45" cy="45" r="20"/><path d="M45 8V13M45 77V82M8 45H13M77 45H82M19 19L23 23M67 67L71 71M19 71L23 67M67 23L71 19"/><path d="M45 55V36M39 42L45 36L51 42M37 55V49H53V55"/></svg>
  <div class="card-title" style="top:156px">Streamline Application<br>Implementation</div>
  <div class="card-text" style="top:220px">Makes system implementations and upgrades easier with better data quality.</div>
  <div class="go" style="top:294px"><svg width="12" height="10" viewBox="0 0 12 10"><path d="M0 5H10M6 1L10 5L6 9" stroke="#fff" stroke-width="1.8" fill="none"/></svg></div>
</div>
<div class="abs card is-featured" style="left:447px;top:1340px;height:373px">
  <svg class="card-bg" width="308" height="373"><polygon points="0,0 308,0 308,319 0,373" fill="#f5ab22"/></svg>
  <svg class="card-icon" style="top:48px" width="90" height="90" viewBox="0 0 90 90" fill="none" stroke="#1b3f7d" stroke-width="2"><circle cx="40" cy="42" r="36"/><circle cx="40" cy="42" r="20"/><circle cx="40" cy="42" r="8"/><path d="M14 20L8 14M66 64L72 70"/></svg>
  <div class="card-title" style="top:156px">Manage Data<br>Effectively</div>
  <div class="card-text" style="top:220px">Effective data management requires expert skills and experience.</div>
  <div class="go" style="top:294px"><svg width="12" height="10" viewBox="0 0 12 10"><path d="M0 5H10M6 1L10 5L6 9" stroke="#fff" stroke-width="1.8" fill="none"/></svg></div>
</div>
<div class="abs card" style="left:777px;top:1340px;height:373px">
  <svg class="card-bg" width="308" height="373"><polygon points="0,0 308,0 308,319 0,373" fill="#fff"/></svg>
  <svg class="card-icon" style="top:58px" width="90" height="90" viewBox="0 0 90 90" fill="none" stroke="#1b3f7d" stroke-width="2"><rect x="4" y="2" width="44" height="76" rx="5"/><path d="M4 66H48"/><path d="M16 34L24 41L36 28"/><path d="M60 44L74 38L74 58Q74 70 60 76Q46 70 46 58L46 38Z" fill="#fff"/><path d="M60 50Q55 57 60 62Q65 57 60 50Z"/></svg>
  <div class="card-title" style="top:166px;left:50px">Future Proof</div>
  <div class="card-text" style="top:220px">New innovations keep you ahead of your competitors.</div>
  <div class="go" style="top:294px"><svg width="12" height="10" viewBox="0 0 12 10"><path d="M0 5H10M6 1L10 5L6 9" stroke="#fff" stroke-width="1.8" fill="none"/></svg></div>
</div>

<!-- row 2 -->
<div class="abs card" style="left:112px;top:1759px;height:374px">
  <svg class="card-bg" width="308" height="374"><polygon points="0,0 308,0 308,320 0,374" fill="#fff"/></svg>
  <svg class="card-icon" style="top:50px;left:27px" width="90" height="90" viewBox="0 0 90 90" fill="none" stroke="#1b3f7d" stroke-width="2"><circle cx="45" cy="10" r="7"/><path d="M35 28Q45 16 55 28"/><circle cx="45" cy="54" r="10"/><circle cx="45" cy="54" r="4"/><circle cx="14" cy="56" r="6"/><path d="M4 76Q14 62 24 76Z"/><circle cx="76" cy="56" r="6"/><path d="M66 76Q76 62 86 76Z"/><path d="M20 34L30 40M70 34L60 40" stroke="#f5ab22"/></svg>
  <div class="card-title" style="top:166px;left:27px">Model Your<br>Organization</div>
  <div class="card-text" style="top:231px;left:27px">Model the way your organization really is, not the way your vendor sees it.</div>
  <div class="go" style="top:294px"><svg width="12" height="10" viewBox="0 0 12 10"><path d="M0 5H10M6 1L10 5L6 9" stroke="#fff" stroke-width="1.8" fill="none"/></svg></div>
</div>
<div class="abs card" style="left:447px;top:1759px;height:374px">
  <svg class="card-bg" width="308" height="374"><polygon points="0,0 308,0 308,320 0,374" fill="#fff"/></svg>
  <svg class="card-icon" style="top:52px;left:29px" width="90" height="90" viewBox="0 0 90 90" fill="none" stroke="#1b3f7d" stroke-width="2"><circle cx="40" cy="42" r="34"/><circle cx="40" cy="42" r="24"/><circle cx="40" cy="34" r="9"/><path d="M24 62Q40 46 56 62"/><path d="M38 50L40 66L42 50"/></svg>
  <div class="card-title" style="top:166px;left:30px">Gain Insights into<br>your Workforce</div>
  <div class="card-text" style="top:231px;left:30px">Provides the platform for strategic analytics and machine learning.</div>
  <div class="go" style="top:294px"><svg width="12" height="10" viewBox="0 0 12 10"><path d="M0 5H10M6 1L10 5L6 9" stroke="#fff" stroke-width="1.8" fill="none"/></svg></div>
</div>
<div class="abs card" style="left:777px;top:1759px;height:374px">
  <svg class="card-bg" width="308" height="374"><polygon points="0,0 308,0 308,320 0,374" fill="#fff"/></svg>
  <svg class="card-icon" style="top:52px;left:29px" width="100" height="90" viewBox="0 0 100 90" fill="none" stroke="#1b3f7d" stroke-width="2"><path d="M14 52Q0 50 2 36Q6 26 18 28Q22 8 44 8Q62 10 66 24Q84 22 88 36Q90 50 74 52"/><circle cx="48" cy="50" r="16"/><circle cx="48" cy="50" r="8"/><circle cx="12" cy="62" r="2"/><circle cx="24" cy="66" r="2"/><circle cx="26" cy="80" r="3"/></svg>
  <div class="card-title" style="top:168px;left:33px">Leverage Cloud-Native<br>Capabilities</div>
  <div class="card-text" style="top:231px;left:30px">Focus on the needs of your business, not the technology.</div>
  <div class="go" style="top:294px"><svg width="12" height="10" viewBox="0 0 12 10"><path d="M0 5H10M6 1L10 5L6 9" stroke="#fff" stroke-width="1.8" fill="none"/></svg></div>
</div>

<!-- cta -->
<div class="abs cta"></div>
<p class="abs cta-line" style="top:2290px">Let us Do The Heavy Lifting So You Can Focus on</p>
<p class="abs cta-line" style="top:2318px">What Matters Most to Your Business</p>
<div class="abs cta-mail">
  <svg width="42" height="38" viewBox="0 0 42 38" aria-hidden="true"><path d="M2 16L21 2L40 16V36H2Z" fill="#1b3f7d"/><rect x="8" y="6" width="26" height="20" fill="#fff"/><text x="21" y="21" text-anchor="middle" font-size="14" font-family="Jost, sans-serif" fill="#f5ab22">@</text><path d="M2 16L21 28L40 16V36H2Z" fill="#2556a8"/></svg>
  <span>sales@veltostaffworks.io</span>
</div>

<!-- footer -->
<div class="abs footer"></div>
<svg class="abs foot-tab" width="265" height="316" aria-hidden="true"><polygon points="0,0 265,0 265,241 0,316" fill="#fff"/></svg>
<div class="abs brand foot-brand" style="flex-direction:column;gap:10px;width:220px;left:134px;top:2540px;text-align:center;font-size:28px">
  <span class="brand-dot" style="width:60px;height:60px"></span>
  <span>Velto Staffworks</span>
</div>

<div class="abs foot-head" style="left:434px;top:2520px">QUICK LINKS</div>
<ul class="abs foot-links">
  <li><b>Home</b></li><li>Our Solutions</li><li>Our Difference</li><li>About Us</li><li>Contact Us</li>
</ul>

<div class="abs foot-head" style="left:618px;top:2520px">CONTACT INFO</div>
<div class="abs contact-row" style="top:2566px"><svg width="14" height="14" viewBox="0 0 14 14"><path d="M3 1L6 4L4.5 6Q6 9 8 9.5L10 8L13 11L11 13Q4 12 1 3Z" fill="#fff"/></svg>555 014 2286</div>
<div class="abs contact-row" style="top:2611px"><svg width="16" height="12" viewBox="0 0 16 12"><rect x="1" y="1" width="14" height="10" fill="none" stroke="#fff" stroke-width="1.5"/><path d="M1 1L8 7L15 1" fill="none" stroke="#fff" stroke-width="1.5"/></svg>www.veltostaffworks.io</div>
<div class="abs contact-row" style="top:2656px"><svg width="14" height="14" viewBox="0 0 14 14"><path d="M7 13Q2 7 2 5A5 5 0 0 1 12 5Q12 7 7 13Z" fill="#fff"/><circle cx="7" cy="5" r="2" fill="#133f83"/></svg>Marlow Ridge, SK</div>

<div class="abs foot-head" style="left:812px;top:2520px">QUICK CONTACT</div>
<div class="abs field" style="left:813px;top:2567px;width:101px;height:33px">Name</div>
<div class="abs field" style="left:919px;top:2567px;width:100px;height:33px">Phone</div>
<div class="abs field" style="left:1024px;top:2567px;width:101px;height:33px">Email</div>
<div class="abs field" style="left:813px;top:2605px;width:312px;height:58px">Message</div>
<div class="abs pill send">Send</div>

<!-- bottom -->
<div class="abs bottom"></div>
<p class="abs copy">Copyright © 2022 Velto Staffworks. All Rights Reserved</p>
<span class="abs social first" style="left:965px" aria-label="Social profile"></span>
<span class="abs social" style="left:1006px" aria-label="Social profile"></span>
<span class="abs social" style="left:1047px" aria-label="Social profile"></span>
<span class="abs social" style="left:1090px" aria-label="Social profile"></span>

</body>
</html>
```